IT company website design

Require a home page and an inner page designed for a company located in Ohio. The company deals with a wide range of IT services like Software development, IT based education services such as digital textbooks and BPO

Would like to get a Home page for the website and an inner page to be designed.

Design must be modern, clean and very professional. The home page should have a carousel of our services for which content will be provided.

It should give a feel that we are a large company to our prospective customers.
Updates

Hi,
In the few designs I have got for the home page, there are mockups with unwanted content/blocks like ex. latest blog posts or similar blocks. Kindly note that, we don't want this. Please follow the information about content on the home page as mentioned in the project brief. Designers, who have already submitted designs, if you can remove the unwanted blocks, it will be really appreciated.

Thanks.

I have received over 9 designs for this project, but none of them seem to be custom designed for my needs. They are just re-use of previous designs and look very out dated. Looking for fresh, clean designs following latest design trends like the ones you see in pixelbazaar etc.

If you can provide me a design that meets my expectations, I can definitely UP my budget for you .

Industry/Entity Type

Education

Requirements
Must have
• > > Home page > >
Home page will have

* Top Menu: Home, About Us, Solutions, Services, Contact us (should have space to accommodate for more)

* Should have a flash carousel/slide show. Each slide should be about a service we provide. Ex. a slide for bpo will have the content "Bridging the quality and cost divide in outsourcing" It should be depicted by an illustration or photograph. If you are going to use photograph, please use ones for framelode.com

* Textual content of about 200 words which we will provide

* Links in the footer along with a copyright, legal notice etc.

* Importantly, the home page should have 2 fancy buttons for "Member Login" and "Online Tutoring"

> > Inner pages > >
Will be mainly textual content explaining each of the service so, should have space for lots of textual content, with a fancy, page title (usually the service name). All inner pages should also have a side menu or something like that from where users can have a one click access to all our services.

Our logo is blue in color. with color code "0080FB". It just a stylized D with rest of the text i.e Quorvane Tech Inc. our logo is of the proportion. 1:5 i.e 60px height, 300px wide. We can proportionately increase or decrease the dimensions as necessary. Color combination of the sight should be something that will go with this.

```html
<!DOCTYPE html>
<html lang="en">
<head>
<meta charset="utf-8">
<title>Quorvane Tech Inc.</title>
<link rel="stylesheet" href="https://fonts.googleapis.com/css2?family=Carlito:wght@400;700&family=Questrial&family=PT+Serif:wght@700&display=swap">
<style>
  :root {
    --brand: #0080fb;
    --nav-link: #1b5fae;
    --bar-dark: #1a1a1a;
    --bar-mid: #2b2b2b;
    --body-text: #454545;
    --frame: #e6e6e6;
    --slide-deep: #05506f;
    --slide-mid: #0e7196;
    --footer-link: #1f86c0;
    --footer-text: #dcdcdc;
    --white: #ffffff;
  }
  * { box-sizing: border-box; margin: 0; padding: 0; }
  html, body { width: 1200px; height: 1066px; overflow: hidden; }
  body {
    position: relative;
    font-family: "Carlito", "Calibri", sans-serif;
    background: linear-gradient(#e3e3e3 482px, #e3e3e3 482px, #f4f4f4 700px, #ffffff 960px);
  }
  .top-bar {
    position: absolute; left: 0; top: 0; width: 1200px; height: 66px;
    background: linear-gradient(90deg, var(--bar-dark), var(--bar-mid) 30%, #202020 55%, var(--bar-mid) 80%, var(--bar-dark));
  }
  .main-nav { position: absolute; left: 130px; top: 14px; display: flex; align-items: center; }
  .main-nav a {
    font-family: "Questrial", sans-serif; font-size: 17px; color: var(--nav-link);
    text-decoration: none; margin-right: 47px; line-height: 40px;
  }
  .main-nav a.is-active {
    width: 88px; height: 40px; text-align: center; color: var(--white);
    background: linear-gradient(#2f95ff, #0a6ee6);
    border: 1px dashed #8cc8ff; outline: 1px solid #0a5fc4; margin-right: 28px;
  }
  .header { position: absolute; left: 0; top: 66px; width: 1200px; height: 416px; background: var(--white); }
  .brand-name {
    position: absolute; left: 135px; top: 100px; font-size: 29px; color: var(--brand);
    font-family: "Carlito", sans-serif; font-weight: 400;
  }
  .action-btn {
    position: absolute; top: 96px; width: 163px; height: 39px; border-radius: 20px;
    background: linear-gradient(#7cc4ff, #2f95ff 45%, #0b73ea 55%, #1d8cff);
    border: 1px solid #0b63c9; color: var(--white); font-size: 14.5px;
    text-align: center; line-height: 37px; text-decoration: none;
  }
  .btn-login { left: 746px; }
  .btn-tutorial { left: 917px; }
  .slider-shadow {
    position: absolute; left: 60px; top: 560px; width: 1080px; height: 50px;
    background: radial-gradient(ellipse at center top, rgba(0,0,0,0.55), rgba(0,0,0,0) 70%);
  }
  .slider-frame { position: absolute; left: 128px; top: 165px; width: 954px; height: 402px; background: var(--frame); }
  .slide {
    position: absolute; left: 9px; top: 9px; width: 936px; height: 384px;
    background: linear-gradient(90deg, #d9d9d6 0%, #c8c2bc 22%, #6f8e9c 40%, var(--slide-mid) 52%, #0a6a8f 75%, var(--slide-deep) 100%);
  }
  .slide-title {
    position: absolute; left: 464px; top: 104px; color: var(--white);
    font-family: "PT Serif", serif; font-weight: 700; line-height: 1;
  }
  .slide-title span { display: block; }
  .t1 { font-size: 66px; letter-spacing: 1px; }
  .t2 { font-size: 52px; margin-top: 0; }
  .t3 { font-size: 46px; margin-top: 2px; }
  .t4 { font-size: 40px; margin-top: 0; }
  .slide-arrow { position: absolute; top: 172px; }
  .arrow-prev { left: 15px; }
  .arrow-next { left: 891px; }
  .slide-dots { position: absolute; left: 448px; top: 360px; }
  .intro { position: absolute; left: 130px; top: 628px; width: 952px; }
  .intro h1 {
    font-family: "Questrial", sans-serif; font-weight: 400; font-size: 26.5px;
    line-height: 30px; color: var(--brand); margin-bottom: 12px;
  }
  .intro p {
    font-size: 15px; line-height: 18px; color: var(--body-text);
    text-align: justify; margin-bottom: 18px; padding-left: 1px;
  }
  .footer-rule { position: absolute; left: 0; top: 962px; width: 1200px; height: 7px; background: #000; }
  .footer {
    position: absolute; left: 0; top: 971px; width: 1200px; height: 95px;
    background: linear-gradient(90deg, var(--bar-dark), var(--bar-mid) 30%, #202020 55%, var(--bar-mid) 80%, var(--bar-dark));
    border-top: 1px solid #555;
  }
  .footer-nav { position: absolute; left: 134px; top: 25px; font-size: 15.5px; color: var(--footer-link); }
  .footer-nav a { color: var(--footer-link); text-decoration: none; }
  .footer-nav .sep { margin: 0 11px; }
  .legal { position: absolute; left: 134px; top: 51px; font-size: 13px; color: var(--footer-text); }
  .legal a { color: var(--footer-link); margin: 0 4px; }
</style>
</head>
<body>
  <header class="top-bar">
    <nav class="main-nav">
      <a href="#" class="is-active">Home</a>
      <a href="#">About Us</a>
      <a href="#">Solutions</a>
      <a href="#">Services</a>
      <a href="#">Contact us</a>
    </nav>
  </header>

  <div class="header"></div>
  <div class="brand-name">Quorvane Tech Inc.</div>
  <a href="#" class="action-btn btn-login">MEMBER LOGIN</a>
  <a href="#" class="action-btn btn-tutorial">ONLINE TUTORIAL</a>

  <div class="slider-shadow"></div>
  <section class="slider-frame">
    <div class="slide" role="img" aria-label="Photograph of a smiling support agent wearing a headset, with colleagues blurred behind her on a blue background"></div>
    <div class="slide-title" style="left:473px;top:113px;">
      <span class="t1">BRIDGING</span>
      <span class="t2">the QUALITY</span>
      <span class="t3">&amp; COST DIVIDE</span>
      <span class="t4">in OUTSOURCING</span>
    </div>
    <svg class="slide-arrow arrow-prev" width="30" height="30" viewBox="0 0 30 30" aria-hidden="true">
      <circle cx="15" cy="15" r="14" fill="#e8e8e8" stroke="#bdbdbd"/>
      <path d="M17 9 L11 15 L17 21" fill="none" stroke="#555" stroke-width="2.5"/>
    </svg>
    <svg class="slide-arrow arrow-next" width="30" height="30" viewBox="0 0 30 30" aria-hidden="true">
      <circle cx="15" cy="15" r="14" fill="#e8e8e8" stroke="#bdbdbd"/>
      <path d="M13 9 L19 15 L13 21" fill="none" stroke="#555" stroke-width="2.5"/>
    </svg>
    <svg class="slide-dots" width="90" height="20" viewBox="0 0 90 20" aria-hidden="true">
      <circle cx="16" cy="10" r="7" fill="#fff"/>
      <circle cx="32" cy="10" r="4" fill="#fff"/>
      <circle cx="48" cy="10" r="4" fill="#fff"/>
      <circle cx="64" cy="10" r="4" fill="#fff"/>
      <circle cx="80" cy="10" r="4" fill="#fff"/>
    </svg>
  </section>

  <main class="intro">
    <h1>Suspendisse at magna leo. Morbi feugiat ultrices nisi eget suscipit. Vivamus iaculis quam nec orci iaculis</h1>
    <p>Phasellus ornare imperdiet ornare. Duis vel placerat magna. Cras elit odio, hendrerit quis mattis eu, accumsan vitae metus. Nulla aliquam urna in mauris scelerisque ac imperdiet elit gravida. Pellentesque augue velit, ultrices non laoreet ac, lobortis tincidunt quam. Sed orci orci, interdum euis­mod cursus et, porttitor in arcu. Maecenas a facilisis augue.</p>
    <p>Duis non commodo sem. Donec sagittis enim vulputate sem adipiscing fringilla. Praesent rhoncus euismod posuere. Proin sagittis varius mi, ut laoreet sem lacinia vestibulum. Donec nec ante non lorem sollicitudin tincidunt.&nbsp; raesent rhoncus euismod posuere. Proin sagittis varius mi, ut laoreet sem lacinia vestibulum.</p>
    <p>Suspendisse ac urna sapien. Donec ornare facilisis egestas. Morbi vel felis at est aliquet ornare nec id massa. In faucibus ornare enim eget porta. Proin et dui purus, sit amet iaculis metus. Curabitur vestibulum, nisi vitae vestibulum imperdiet, quam augue pretium ipsum, quis varius nisi est sed felis. Cras nunc massa, tincidunt quis rutrum eget, lobortis consectetur enim. Sed fringilla placerat nunc id mattis.</p>
  </main>

  <div class="footer-rule"></div>
  <footer class="footer">
    <nav class="footer-nav">
      <a href="#">Home</a><span class="sep">|</span><a href="#">About Us</a><span class="sep">|</span><a href="#">Solutions</a><span class="sep">|</span><a href="#">Services</a><span class="sep">|</span><a href="#">Contact us</a>
    </nav>
    <p class="legal">copyright 2011 Quorvane Tech Inc. &nbsp;<a href="#">Privacy Policy</a>|<a href="#">Terms and Policies</a></p>
  </footer>
</body>
</html>
```